QuillNest - Home Income and Business Resources Platform

I am looking for a website template for a multi-purposed website. This website will feature:

1.) Website Directory with Ratings & comments on listings
2.) Company Blog
3.) Homepage with Content (see files for homepage mock)

I would like the Design to have a default width 1170px (wider then normal)

Of course I am looking for Pages for Listings to be designed.

Great looking BLOG Layout: http://journal.pagecrafter.example/html/blog.html

I would like 4 Versions of a Website Directory Listing "Box"
1.) Basic Listing Box
2.) Sponsored Listing Box
3.) Recommended Listing Box
4.) Stay Away From Listing Box

Information on the Listing Page (Like on a Category Page)
Site Name, Site URL, Website Image, # of Views, Rating and # of Comments

Information on the Listing Details Page:
Same as ABOVE + About website Description, Orvix Rank, Category Information

Decent looking examples is here: https://samples.kavlora.example/directory/computers/ and http://www.brimlisting.example/.

I will include some sketches and screenshots of things I like/looking for. As designers,you have creative freedom and are encouraged to show this. This is Phase one of this project and winning designer is guaranteed to have future work for this project.

Target Market(s)

Directory, business, websites

Industry/Entity Type

Business

Coding

Number of Pages Required

5+ page

Font styles to use
Sans Serif

Colors

Designer to choose colors to be used in the design.

Requirements
Must have
• Professional yet clean look. The use of Icons & images
• Unique Look
Should not have
• Any exact copies of any examples I provided

```html
<!DOCTYPE html>
<html lang="en">
<head>
<meta charset="utf-8">
<title>QuillNest – Home Income and Business Resources</title>
<link href="https://fonts.googleapis.com/css2?family=Open+Sans:wght@400;600;700&family=Raleway:wght@300;400;500&display=swap" rel="stylesheet">
<style>
:root{
  --page-bg:#e9f2fc;
  --card-bg:#ffffff;
  --brand-blue:#1a6fd1;
  --link-blue:#1e88e5;
  --heading-blue:#1b74c9;
  --accent-orange:#ff6f1a;
  --text-dark:#222;
  --text-body:#5a5a5a;
  --rule:#d8dde3;
  --footer-text:#6b7280;
}
*{box-sizing:border-box;margin:0;padding:0}
html,body{width:745px;height:1200px;overflow:hidden}
body{background:var(--page-bg);font-family:"Open Sans",sans-serif;color:var(--text-body);position:relative}
.abs{position:absolute}

/* header */
.top-header{left:0;top:0;width:745px;height:34px;background:#f5f9fe}
.brand{left:28px;top:9px;display:flex;align-items:center;gap:5px}
.brand-dot{width:9px;height:9px;border-radius:50%;background:var(--accent-orange)}
.brand-name{font-family:"Open Sans",sans-serif;font-weight:600;font-size:11px;color:var(--brand-blue);line-height:1}
.brand-tag{left:42px;top:21px;font-size:5.5px;color:#333}
.phone{right:28px;top:13px;font-size:9px;color:#555;display:flex;align-items:center;gap:3px}
.main-nav{left:28px;top:34px;width:689px;height:22px;background:var(--brand-blue);display:flex;align-items:center}
.main-nav a{color:#fff;text-decoration:none;font-size:8px;font-weight:600;padding:0 5px;height:22px;line-height:22px}
.main-nav a.active{background:var(--accent-orange)}
.main-nav .first{padding-left:8px}
.nav-social{margin-left:auto;display:flex;gap:6px;padding-right:8px}
.nav-social span{width:6px;height:6px;background:#fff;border-radius:1px}

/* posts */
.post-card{left:28px;width:423px;height:217px;background:var(--card-bg);display:flex}
.post-image{width:156px;height:217px;flex:none}
.post-body{flex:1;padding:12px 11px 0 12px;position:relative}
.post-title{font-family:"Raleway",sans-serif;font-weight:400;font-size:14px;line-height:15.5px;color:var(--text-dark);text-align:center;padding:0 20px}
.title-rule{width:30px;height:1px;background:#333;margin:5px auto 5px}
.post-cat{text-align:center;font-size:7.2px;color:var(--brand-blue)}
.post-text{font-size:7.9px;line-height:13.6px;text-align:justify;margin-top:10px;color:var(--text-body)}
.post-meta{font-size:7.9px;margin-top:10px;color:#444}
.post-meta b{font-weight:400;color:var(--link-blue)}
.post-foot{position:absolute;left:0;right:0;bottom:0;height:48px;border-top:1px solid var(--rule);display:flex;align-items:center;padding:0 12px}
.btn{display:inline-block;width:96px;height:24px;line-height:24px;text-align:center;color:#fff;font-size:8px;border-radius:1px;text-decoration:none}
.btn-orange{background:var(--accent-orange)}
.btn-blue{background:var(--brand-blue)}
.post-stats{margin-left:auto;display:flex;gap:10px;font-size:7.5px;color:#444;align-items:center}
.post-stats span{display:flex;align-items:center;gap:4px}

/* sidebar */
.sidebar{left:481px;top:79px;width:235px;height:759px;background:var(--card-bg)}
.avatar{left:73px;top:13px;width:89px;height:89px;border-radius:50%;background:radial-gradient(circle at 50% 45%,#c98b67,#7a3b2a 60%,#ddd 62%);border:3px solid #e3e3e3}
.side-heading{width:235px;text-align:center;font-family:"Raleway",sans-serif;font-weight:500;font-size:13.5px;color:var(--heading-blue)}
.side-rule{left:-2px;width:235px;height:1px;background:var(--rule)}
.about-text{left:14px;top:130px;width:207px;font-size:7.9px;line-height:13.6px;text-align:justify}
.social-row{left:43px;top:264px;display:flex;gap:15px}
.social-row span{width:18px;height:18px;background:var(--link-blue);border-radius:1px;position:relative}
.social-row span:after{content:"";position:absolute;left:6px;bottom:-4px;border:3px solid transparent;border-top-color:var(--link-blue);border-bottom:none}
.follow{width:235px;text-align:center;top:294px;font-size:7px;color:#333}
.recent-img{left:10px;top:356px;width:215px;height:74px;background:linear-gradient(90deg,#8a6b3a,#b79a5c 45%,#d9b9a4 70%,#6f7d3d)}
.recent-title{width:235px;top:437px;text-align:center;font-size:8.2px;font-weight:700;color:var(--link-blue)}
.recent-date{width:235px;top:455px;text-align:center;font-size:7.5px;color:#333}
.pager{left:101px;top:484px;display:flex;gap:1px}
.pager span{width:16px;height:16px;background:var(--accent-orange);display:flex;align-items:center;justify-content:center}
.ad-box{left:12px;top:557px;width:212px;height:180px;background:linear-gradient(180deg,#151515,#0b0b0b 60%,#1c1c1c);padding:14px 10px}
.ad-title{font-family:"Raleway",sans-serif;font-weight:300;font-size:29px;line-height:32px;color:#fff}
.ad-text{margin-top:10px;font-size:7.9px;line-height:12.4px;color:#fff;text-align:justify}

/* features */
.feature{top:862px;width:217px;height:300px;background:linear-gradient(180deg,#f6f9fd 55%,#e6eef8);border:1px solid #b9d2ee}
.feature-icon{left:72px;top:-1px;width:72px;height:64px;border-radius:0 0 36px 36px;background:#fff;box-shadow:0 4px 6px rgba(0,0,0,.15);display:flex;align-items:center;justify-content:center}
.feature-icon i{width:38px;height:34px;border-radius:50%;display:block}
.feature-title{left:9px;top:84px;font-family:"Raleway",sans-serif;font-weight:500;font-size:12px;color:var(--heading-blue)}
.feature-text{left:9px;top:105px;width:198px;font-size:7.9px;line-height:14px;text-align:justify}
.feature .btn{position:absolute;left:9px;top:242px}

/* footer */
.footer-rule{left:0;top:1178px;width:745px;height:1px;background:#b9c6d6}
.footer-social{left:28px;top:1186px;display:flex;gap:4px}
.footer-social span{width:6px;height:6px;background:#777;border-radius:1px}
.footer-links{left:72px;top:1184px;display:flex;gap:8px;font-size:7.2px;color:var(--footer-text)}
.copyright{right:28px;top:1184px;font-size:7.2px;color:var(--footer-text)}
</style>
</head>
<body>

<header>
  <div class="abs top-header"></div>
  <div class="abs brand"><span class="brand-dot"></span><span class="brand-name">QuillNest</span></div>
  <div class="abs brand-tag">Home Income and Business Resources</div>
  <div class="abs phone">
    <svg width="7" height="7" viewBox="0 0 10 10"><path d="M2 0l2 2.5-1.2 1.3a6 6 0 003.4 3.4L7.5 6 10 8 8.7 9.6C4.5 9.8.2 5.5.4 1.3z" fill="#1a6fd1"/></svg>
    0800-555-010-020
  </div>
  <nav class="abs main-nav">
    <a class="first" href="#">HOME</a><a href="#">ABOUT</a><a class="active" href="#">LISTING</a><a href="#">LISTING DETAILS</a><a href="#">CONTACT</a>
    <div class="nav-social"><span></span><span></span><span></span></div>
  </nav>
</header>

<main>
  <article class="abs post-card" style="top:81px">
    <div class="post-image" role="img" aria-label="Tablet screen showing a line chart and pie chart" style="background:linear-gradient(100deg,#cfd6de,#eef1f4 40%,#a9b3bf 80%,#6b4f3a)"></div>
    <div class="post-body">
      <h2 class="post-title">Chronic Illness and Starting a Business Resources</h2>
      <div class="title-rule"></div>
      <div class="post-cat">Business Resources</div>
      <p class="post-text">Your general health is intimately connected with the foods and drinks you put into your body. Each person is unique in what food or drink can trigger feeling unhealthy and rundown. It is very easy to lose track of which foods and drinks can be wreaking havoc with your health. A great way to do some detective work</p>
      <p class="post-meta">Written by <b>Orvix Rank</b> in <b>June 21, 2017</b></p>
      <div class="post-foot">
        <a class="btn btn-orange" href="#">Read More</a>
        <div class="post-stats">
          <span><svg width="9" height="8" viewBox="0 0 10 9"><ellipse cx="5" cy="4" rx="5" ry="3.6" fill="#1e88e5"/><path d="M2 6l-1 3 3-2z" fill="#1e88e5"/></svg>05</span>
          <span><svg width="9" height="8" viewBox="0 0 10 9"><path d="M5 9L.8 4.6A2.5 2.5 0 015 1.3a2.5 2.5 0 014.2 3.3z" fill="#1e88e5"/></svg>02</span>
        </div>
      </div>
    </div>
  </article>

  <article class="abs post-card" style="top:330px">
    <div class="post-image" role="img" aria-label="Modern two-storey house lit at dusk beside a pool" style="background:linear-gradient(180deg,#5b4a78,#8a6a6f 35%,#c58d5e 60%,#3a3450)"></div>
    <div class="post-body">
      <h2 class="post-title">Chronic Illness and Starting a Home Income</h2>
      <div class="title-rule"></div>
      <div class="post-cat">Home Income</div>
      <p class="post-text">Your general health is intimately connected with the foods and drinks you put into your body. Each person is unique in what food or drink can trigger feeling unhealthy and rundown. It is very easy to lose track of which foods and drinks can be wreaking havoc with your health. A great way to do some detective work</p>
      <p class="post-meta">Written by <b>Orvix Rank</b> in <b>June 21, 2017</b></p>
      <div class="post-foot">
        <a class="btn btn-blue" href="#">Read More</a>
        <div class="post-stats">
          <span><svg width="9" height="8" viewBox="0 0 10 9"><ellipse cx="5" cy="4" rx="5" ry="3.6" fill="#1e88e5"/><path d="M2 6l-1 3 3-2z" fill="#1e88e5"/></svg>05</span>
          <span><svg width="9" height="8" viewBox="0 0 10 9"><path d="M5 9L.8 4.6A2.5 2.5 0 015 1.3a2.5 2.5 0 014.2 3.3z" fill="#1e88e5"/></svg>02</span>
        </div>
      </div>
    </div>
  </article>

  <article class="abs post-card" style="top:575px">
    <div class="post-image" role="img" aria-label="Keyboard and tablet calendar on a wooden desk" style="background:linear-gradient(120deg,#e8e8e6,#c9cbcc 45%,#7a4e35 75%,#5a3624)"></div>
    <div class="post-body">
      <h2 class="post-title">Chronic Illness and Starting an Exercise Regimen</h2>
      <div class="title-rule"></div>
      <div class="post-cat">Business Resources</div>
      <p class="post-text">Your general health is intimately connected with the foods and drinks you put into your body. Each person is unique in what food or drink can trigger feeling unhealthy and rundown. It is very easy to lose track of which foods and drinks can be wreaking havoc with your health. A great way to do some detective work</p>
      <p class="post-meta">Written by <b>Orvix Rank</b> in <b>June 21, 2017</b></p>
      <div class="post-foot">
        <a class="btn btn-orange" href="#">Read More</a>
        <div class="post-stats">
          <span><svg width="9" height="8" viewBox="0 0 10 9"><ellipse cx="5" cy="4" rx="5" ry="3.6" fill="#1e88e5"/><path d="M2 6l-1 3 3-2z" fill="#1e88e5"/></svg>05</span>
          <span><svg width="9" height="8" viewBox="0 0 10 9"><path d="M5 9L.8 4.6A2.5 2.5 0 015 1.3a2.5 2.5 0 014.2 3.3z" fill="#1e88e5"/></svg>02</span>
        </div>
      </div>
    </div>
  </article>

  <aside class="abs sidebar">
    <div class="abs avatar" role="img" aria-label="Portrait photo of the site author"></div>
    <h3 class="abs side-heading" style="top:107px">About Us</h3>
    <p class="abs about-text">Lorem Ipsum is simply dummy text of the printing and typesetting industry. Lorem Ipsum has been the industry's standard dummy text ever since the 1500s, when an wn printer took a galley of type and scram-bled it to</p>
    <h3 class="abs side-heading" style="top:218px">Social Media</h3>
    <div class="abs side-rule" style="top:240px"></div>
    <div class="abs social-row"><span></span><span></span><span></span><span></span><span></span></div>
    <div class="abs follow">Follow Us</div>
    <h3 class="abs side-heading" style="top:315px">Recent Posts</h3>
    <div class="abs side-rule" style="top:338px"></div>
    <div class="abs recent-img" role="img" aria-label="Woman blowing bubbles in a sunny field"></div>
    <div class="abs recent-title">Regular Exercise is a Natural Anti-Inflammatory</div>
    <div class="abs recent-date">August 22, 2016</div>
    <div class="abs pager">
      <span><svg width="6" height="8" viewBox="0 0 6 8"><path d="M5 0L1 4l4 4" fill="none" stroke="#fff" stroke-width="1.4"/></svg></span>
      <span><svg width="6" height="8" viewBox="0 0 6 8"><path d="M1 0l4 4-4 4" fill="none" stroke="#fff" stroke-width="1.4"/></svg></span>
    </div>
    <h3 class="abs side-heading" style="top:520px">Hey Warriors, We Support You!</h3>
    <div class="abs side-rule" style="top:542px"></div>
    <div class="abs ad-box">
      <div class="ad-title">Advertising Benefits</div>
      <p class="ad-text">Action plan chronic chronic illness chronic illness pain chronic pain coping with a chronic illness depression employment energy failure fibro fibro-myalgia focus food diary functional medicine goal action plan goals inflammation invisible illness job job hunting life goals</p>
    </div>
  </aside>

  <section class="abs feature" style="left:27px">
    <div class="abs feature-icon" role="img" aria-label="Icon of a house held in a hand"><i style="background:#f3a25a"></i></div>
    <h3 class="abs feature-title">Home Income Resource Directory</h3>
    <p class="abs feature-text">Text: Find what you need, when you need it.The QuillNest website directory is your one-stop pit for anything involved in making money from home marketing your business or finding a opportunity. Our modern, community supported directory will help a sensibl Lorem Ipsum is simply dummy text of the printing and typesettin industry. Lorem Ipsum has been the industry's standard dummy text ever since the 1500s, when an unknown printer took a</p>
    <a class="btn btn-orange" href="#">Read More</a>
  </section>
  <section class="abs feature" style="left:264px">
    <div class="abs feature-icon" role="img" aria-label="Icon of a presentation board with a bar chart"><i style="background:#4f7fb8"></i></div>
    <h3 class="abs feature-title">Advertising Benefits</h3>
    <p class="abs feature-text">Text: Everyone needs to advertise and we know just how to get your offer out to the right people. We have many methods including: Text ads, E-mail, Display, newsletter and even some old school methods available to make your next campaign a success. Advertise a website, a link text, full page circular or a small account manager that will handle everything Lorem Ipsum is simply dummy text of the printing and typesetting industry. dummy text ever</p>
    <a class="btn btn-blue" href="#">Read More</a>
  </section>
  <section class="abs feature" style="left:500px">
    <div class="abs feature-icon" role="img" aria-label="Icon of a hand holding a coin"><i style="background:#f2b53c"></i></div>
    <h3 class="abs feature-title">Earning With QuillNest</h3>
    <p class="abs feature-text">Text: Join QuillNest and start earning money. When you share QuillNest and lock in an advertiser or premium listing, we reward you. Build a downline at any of our listed sites when you share QuillNest with NO extra work. Its all done for you.We also offer a of our is the printing and typesetting industry. Lorem Ipsum has been the industry's standard dummy text ever since the 1500s, when an unknown printer took a galley esetting industry. Lorem</p>
    <a class="btn btn-orange" href="#">Read More</a>
  </section>
</main>

<footer>
  <div class="abs footer-rule"></div>
  <div class="abs footer-social"><span></span><span></span><span></span></div>
  <div class="abs footer-links"><span>About Us</span><span>Privacy Policy</span><span>Terms of Use</span><span>Advertise Us</span><span>Help</span></div>
  <div class="abs copyright">© 2017 Copyright</div>
</footer>

</body>
</html>
```